Luxury 8’x4’ Acreage FOR SALE sign

I need (in 3 days) an outstanding Luxury - looking For Sale sign with my logo prominent & my brokerage logo to make up 9% of the total design space. It also needs to have “space” around it to breathe (as per brokerage qualification boundaries) It needs to be unique , have my phone number , my logo (with or without Real Estate cropped out) , brokerage logo & “for sale” or “available” or some type of wording that projects it’s a sign listing an acreage. My main focus is branding - MY logo & brand being recognized. I am unsure about including a photo of myself or not as I need this to look sleek & not busy! I have included a photo of the sign I designed & it’s just not doing it for me … I DO NOT want it to look like a business card. I’m finding it hard to make it look intentional with the DVK logo needed. It can be either logo - the box logo or the horizontal DVK logo but MUST make up 9%.
Updates

No photo of me please ! Decision made!

Target Market(s)

Luxury

Industry/Entity Type

Real Estate

Requirements
Must have
• Phone number, My logo, My Brokerage logo
Nice to have
• Needs to stand out “for sale” or “available” or

```html
<!DOCTYPE html>
<html lang="en">
<head>
<meta charset="utf-8">
<title>Maren Solvik Real Estate – For Sale Sign</title>
<link rel="stylesheet" href="https://fonts.googleapis.com/css2?family=Cinzel:wght@600;700&family=Montserrat:wght@800&display=swap">
<style>
  :root {
    --ink: #050709;
    --paper: #ffffff;
    --gold-light: #f3e07a;
    --gold-mid: #e8c45a;
    --gold-deep: #dca63c;
    --stage-light: #d4d4d6;
    --stage-dark: #6e6e72;
  }
  * { margin: 0; padding: 0; box-sizing: border-box; }
  html, body { width: 1200px; height: 676px; overflow: hidden; }
  body {
    position: relative;
    background: linear-gradient(110deg, var(--stage-light) 0%, #a4a4a7 50%, var(--stage-dark) 100%);
  }
  .sign {
    position: absolute;
    left: 76px; top: 73px;
    width: 1048px; height: 524px;
    background: var(--paper);
    overflow: hidden;
  }
  .sign-head {
    position: absolute; left: 0; top: 0;
    width: 100%; height: 388px;
    background: var(--ink);
  }
  .gold-band {
    position: absolute; left: 0; top: 388px;
    width: 100%; height: 9px;
    background: linear-gradient(90deg, var(--gold-light), var(--gold-mid) 50%, var(--gold-deep));
  }
  .agent-brand {
    position: absolute; left: 62px; top: 58px;
    width: 590px;
    font-family: "Cinzel", serif;
    font-weight: 700;
    color: var(--paper);
    text-align: right;
    line-height: 1;
  }
  .agent-first { display: block; font-size: 104px; margin-right: 6px; }
  .agent-last { display: block; font-size: 118px; margin-top: 6px; letter-spacing: -1px; }
  .agent-tag {
    display: block; font-size: 50px; margin-top: 20px;
    letter-spacing: 23px; margin-right: -23px; text-align: center;
  }
  .divider {
    position: absolute; left: 731px; top: 72px;
    width: 2px; height: 254px;
    background: linear-gradient(180deg, transparent, var(--gold-deep) 30%, var(--gold-deep) 70%, transparent);
  }
  .broker-box {
    position: absolute; left: 769px; top: 101px;
    width: 227px; height: 194px;
    background: #000;
    display: flex; flex-direction: column; align-items: center; justify-content: center;
    font-family: "Cinzel", serif; font-weight: 700; color: var(--paper);
    line-height: 1;
  }
  .broker-name { font-size: 72px; }
  .broker-sub { font-size: 30px; margin-top: 14px; }
  .listing-status {
    position: absolute; left: 62px; top: 418px;
    font-family: "Cinzel", serif; font-weight: 700;
    font-size: 82px; line-height: 1; color: #000;
    letter-spacing: -1px;
  }
  .contact {
    position: absolute; left: 498px; top: 433px;
    display: flex; align-items: center; gap: 14px;
  }
  .contact-icon { width: 54px; height: 54px; display: block; }
  .contact-phone {
    font-family: "Montserrat", sans-serif; font-weight: 800;
    font-size: 62px; line-height: 1; color: #000; letter-spacing: -1px;
  }
</style>
</head>
<body>
  <main class="sign">
    <section class="sign-head">
      <h1 class="agent-brand">
        <span class="agent-first">MAREN</span>
        <span class="agent-last">SOLVIK</span>
        <span class="agent-tag">REAL ESTATE</span>
      </h1>
      <div class="divider"></div>
      <div class="broker-box">
        <span class="broker-name">DVK</span>
        <span class="broker-sub">REALTY</span>
      </div>
    </section>
    <div class="gold-band"></div>
    <p class="listing-status">FOR SALE</p>
    <div class="contact">
      <svg class="contact-icon" viewBox="0 0 54 54" aria-hidden="true">
        <defs>
          <linearGradient id="gold-disc" x1="0" y1="0" x2="1" y2="1">
            <stop offset="0" stop-color="#f3e07a"/>
            <stop offset="1" stop-color="#dca63c"/>
          </linearGradient>
        </defs>
        <circle cx="27" cy="27" r="27" fill="url(#gold-disc)"/>
        <path d="M17 15c2-2 4-1 5 1l2 4c1 2 0 3-1 4l-1 1c1 3 4 6 7 7l1-1c1-1 2-2 4-1l4 2c2 1 3 3 1 5l-2 2c-3 2-9 0-15-6s-8-12-6-15z" fill="#000"/>
        <path d="M29 16a9 9 0 0 1 9 9M29 11a14 14 0 0 1 14 14" fill="none" stroke="#000" stroke-width="2.4" stroke-linecap="round"/>
      </svg>
      <span class="contact-phone">403-555-0142</span>
    </div>
  </main>
</body>
</html>
```